Bright Haven Estate Sales web design

We are looking to launch an Estate Sales Website for Nashville, TN. The name of our Business is Bright Haven Estate Sales. We would like to give you a blank slate so that you can showcase your design skills for us. The few things we are looking for are a nice header graphic of a house or a stock image of an estate sale. Near the header graphic we would like a quick inquiry form. If not on the right side of the header maybe midway down the site. We potentially want to see what purple and Gold look like on the site however this is not a must. We have over 20 years of industry related experience.

1. Buttons at top of the website will be.
a. Services
b. Upcoming Sales
c. About Us
d. FAQs
e. Resources

Services we offer:
1. Estate Sales
2. Cleanouts
3. Appraisals

Sites We like:
https://www.corvellestatesales.example/

We don't have a logo yet so if you have ideas please share them with us. Below are 2 ideas however if you have your own thoughts please ignore.

1. Oval ornate frame, gold and black, with BHES in the middle, deep purple. Think of catering to high class people..font should be fancy as opposed to simple.

2. Another option, Bright Haven in bold fancy script, same colors, with Estate Sales below, small different font, black.

```html
<!DOCTYPE html>
<html lang="en">
<head>
<meta charset="utf-8">
<title>Bright Haven Estate Sales</title>
<link rel="stylesheet" href="https://fonts.googleapis.com/css2?family=Libre+Baskerville:wght@400;700&family=Poppins:wght@400;500;600&display=swap">
<style>
:root{
  --gold:#fcd200;
  --purple:#5a2d91;
  --ink:#1b1b1b;
  --text:#3d3d3d;
  --cream:#fffbe9;
  --lavender:#f5f4fa;
  --field:#efefef;
  --footer:#1c1c1c;
}
*{box-sizing:border-box;margin:0;padding:0}
html,body{width:1200px;height:3241px;overflow:hidden}
body{position:relative;background:#fff;font-family:'Poppins',sans-serif;color:var(--ink)}
.abs{position:absolute}
.serif{font-family:'Libre Baskerville',serif}
.btn{position:absolute;background:var(--gold);color:var(--ink);font-weight:600;font-size:13px;display:flex;align-items:center;justify-content:center}

/* header */
.site-header{position:absolute;left:0;top:0;width:1200px;height:70px;background:#fff;z-index:3}
.brand{position:absolute;left:141px;top:20px;display:flex;align-items:center;gap:9px}
.brand-mark{width:22px;height:22px;background:var(--gold)}
.brand-name{font-family:'Poppins',sans-serif;font-weight:600;font-size:20px;color:var(--purple)}
.main-nav a{position:absolute;top:27px;font-size:13px;font-weight:500;color:var(--ink);text-decoration:none}

/* hero */
.hero-photo{position:absolute;left:0;top:70px;width:1200px;height:560px;background:linear-gradient(100deg,#3b3a37 0%,#5e5b55 40%,#8b877e 70%,#c8c6c0 100%)}
.hero-tick{left:141px;top:186px;width:48px;height:6px;background:var(--gold)}
.hero-title{left:141px;top:236px;font-family:'Libre Baskerville',serif;font-weight:700;font-size:62px;line-height:1;color:var(--gold)}
.hero-sub{left:141px;top:310px;font-family:'Libre Baskerville',serif;font-size:44px;line-height:1;color:#fff}
.hero-tag{left:141px;top:380px;font-size:16px;color:#fff}
.inquiry{position:absolute;left:720px;top:142px;width:344px;height:357px;background:#fff}
.inquiry .kicker{position:absolute;top:24px;width:100%;text-align:center;font-size:12.5px}
.inquiry h3{position:absolute;top:48px;width:100%;text-align:center;font-size:16.5px;font-weight:600}
.inquiry .rule{position:absolute;left:137px;top:77px;width:70px;height:2px;background:var(--gold)}
.field{position:absolute;height:39px;background:var(--field);font-size:11.5px;color:#777;display:flex;align-items:center;padding-left:14px}
.field svg{position:absolute;right:12px;top:14px}

/* sections */
.section-tick{position:absolute;width:34px;height:5px;background:var(--gold)}
.section-title{position:absolute;left:0;width:1200px;text-align:center;font-family:'Libre Baskerville',serif;font-size:28px}
.photo{position:absolute}
.about-copy{position:absolute;left:647px;width:415px;font-size:13.3px;line-height:22.6px;color:var(--text)}
.badge{position:absolute;left:308px;top:967px;width:145px;height:118px;background:#fff;box-shadow:0 4px 16px rgba(0,0,0,.08)}
.service-card{position:absolute;top:1321px;width:291px;height:226px;background:var(--cream);text-align:center}
.service-card h4{position:absolute;top:116px;width:100%;font-family:'Libre Baskerville',serif;font-weight:400;font-size:17px}
.service-card p{position:absolute;top:150px;left:25px;width:241px;font-size:11.5px;line-height:20px;color:var(--text)}
.service-card svg.icon{position:absolute;left:110px;top:20px}
.card-arrow{position:absolute;top:204px;left:125px;width:42px;height:41px;background:var(--gold);display:flex;align-items:center;justify-content:center}

.testimonials{position:absolute;left:0;top:1652px;width:1200px;height:487px;background:var(--lavender)}
.avatar{position:absolute;border-radius:50%;border:3px solid var(--lavender)}
.quote{position:absolute;left:300px;top:1955px;width:600px;text-align:center;font-size:13px;line-height:22.6px;color:var(--text)}

.sale{position:absolute;top:2352px;width:292px}
.sale .pic{height:222px}
.sale h5{margin-top:19px;font-size:16px;font-weight:600;display:flex;justify-content:space-between;align-items:center;padding-right:14px}
.sale .loc{margin-top:8px;font-size:12.5px;color:var(--text);display:flex;align-items:center;gap:8px}
.sale .date{margin-top:14px;font-size:12.5px;font-weight:500}
.sale .more{margin-top:14px;font-size:14px;font-weight:500;color:var(--purple);display:flex;align-items:center;gap:8px}
.sale .more span{text-decoration:underline}

/* footer */
.footer-brand{left:141px;top:3030px;font-family:'Poppins',sans-serif;font-weight:600;font-size:38px;line-height:1.15;color:#fff}
.footer-mark{left:210px;top:2940px;width:40px;height:40px;background:var(--gold)}
.footer-col{position:absolute;top:2920px}
.footer-col h6{font-family:'Libre Baskerville',serif;font-weight:400;font-size:18px;color:var(--gold);margin-bottom:14px}
.footer-col a{display:block;font-size:13px;color:#fff;line-height:29px;text-decoration:none}
.contact-row{display:flex;gap:12px;font-size:13px;color:#fff;line-height:19px;margin-bottom:10px}
.footer-rule{left:141px;top:3183px;width:918px;height:1px;background:#444}
.copyright{left:141px;top:3203px;font-size:13px;color:#fff}
.social{position:absolute;top:3200px;width:26px;height:26px;border-radius:50%;background:#fff}
</style>
</head>
<body>

<header class="site-header">
  <div class="brand"><span class="brand-mark"></span><span class="brand-name">Bright Haven</span></div>
  <nav class="main-nav">
    <a style="left:515px">Home</a>
    <a style="left:578px">About Us</a>
    <a style="left:660px">Services</a>
    <a style="left:740px">Sales</a>
    <a style="left:798px">FAQ’s</a>
    <a style="left:858px">Resources</a>
  </nav>
  <div class="btn" style="left:950px;top:18px;width:109px;height:35px">Contact Us</div>
</header>

<section class="hero">
  <div class="hero-photo" role="img" aria-label="Hands passing a house key over a model house on a desk"></div>
  <svg class="abs" style="left:0;top:500px" width="1200" height="132" viewBox="0 500 1200 132">
    <polygon points="0,528 600,616 1200,528 1200,545 600,628 0,545" fill="#fcd200"/>
    <polygon points="0,545 600,628 1200,545 1200,632 0,632" fill="#fff"/>
  </svg>
  <svg class="abs" style="left:588px;top:538px" width="24" height="42" viewBox="0 0 24 42">
    <rect x="3" y="2" width="18" height="28" rx="9" fill="#fff"/>
    <rect x="10.5" y="8" width="3" height="8" rx="1.5" fill="#333"/>
    <path d="M7 34l5 5 5-5" stroke="#fff" stroke-width="2.5" fill="none"/>
  </svg>
  <div class="abs hero-tick"></div>
  <h1 class="abs hero-title">Bright Haven</h1>
  <div class="abs hero-sub">Estate Sales</div>
  <p class="abs hero-tag">Nashville's Premier Estate Sale Company.</p>
  <div class="btn" style="left:141px;top:430px;width:109px;height:34px">Learn More</div>

  <form class="inquiry">
    <p class="kicker">Request More Information About</p>
    <h3>Bright Haven Estate Sales</h3>
    <div class="rule"></div>
    <div class="field" style="left:21px;top:103px;width:302px">Full Name*</div>
    <div class="field" style="left:21px;top:152px;width:302px">Email Address*</div>
    <div class="field" style="left:21px;top:201px;width:302px">Phone Number*</div>
    <div class="field" style="left:21px;top:250px;width:143px">Price Range
      <svg width="12" height="8" viewBox="0 0 12 8"><path d="M1 1l5 5 5-5" stroke="#222" stroke-width="1.6" fill="none"/></svg></div>
    <div class="field" style="left:179px;top:250px;width:144px">Property Type
      <svg width="12" height="8" viewBox="0 0 12 8"><path d="M1 1l5 5 5-5" stroke="#222" stroke-width="1.6" fill="none"/></svg></div>
    <div class="btn" style="left:21px;top:301px;width:302px;height:35px">Schedule a Consultation</div>
  </form>
</section>

<section class="about">
  <div class="photo" style="left:141px;top:794px;width:209px;height:311px;background:linear-gradient(160deg,#5a4434,#2a221d 60%,#8b7a6a)" role="img" aria-label="Keys handed over a signed contract"></div>
  <div class="photo" style="left:367px;top:723px;width:208px;height:311px;background:linear-gradient(180deg,#e9e9e9,#c9ccd1 55%,#6d7b93)" role="img" aria-label="Couple shaking hands with an agent"></div>
  <div class="badge">
    <svg class="abs" style="left:12px;top:22px" width="48" height="46" viewBox="0 0 48 46">
      <circle cx="24" cy="24" r="11" fill="none" stroke="#fcd200" stroke-width="2"/>
      <circle cx="24" cy="24" r="5" fill="none" stroke="#fcd200" stroke-width="2"/>
      <path d="M18 34l-4 10 6-3 4 4 M30 34l4 10-6-3-4 4" stroke="#fcd200" stroke-width="2" fill="none"/>
      <path d="M24 2l2 4 4 .5-3 3 1 4-4-2-4 2 1-4-3-3 4-.5z" fill="#fcd200"/>
      <path d="M6 12l1.5 3 3 .4-2.2 2 .6 3-2.9-1.5-2.9 1.5.6-3-2.2-2 3-.4z M42 12l1.5 3 3 .4-2.2 2 .6 3-2.9-1.5-2.9 1.5.6-3-2.2-2 3-.4z" fill="#fcd200"/>
    </svg>
    <div class="abs serif" style="left:68px;top:26px;font-size:44px;font-weight:700;color:var(--gold);line-height:1">20</div>
    <div class="abs" style="left:12px;top:82px;font-size:14px;font-weight:600">Years Experience</div>
  </div>
  <div class="section-tick" style="left:647px;top:737px"></div>
  <h2 class="abs serif" style="left:647px;top:774px;font-size:28px;font-weight:400">About Bright Haven</h2>
  <p class="about-copy" style="top:832px">It is a long established fact that a reader will be distracted by the readable content of a page when looking at its layout. The point of using Lorem Ipsum is that it has a more-or-less normal distribution of letters, as opposed to using 'Content here, content here', making it look like readable English.</p>
  <p class="about-copy" style="top:959px">There are many variations of passages of Lorem Ipsum available, but the majority have suffered alteration in some form, by injected humour, or randomised words which don't look even slightly believable.</p>
  <div class="btn" style="left:647px;top:1072px;width:108px;height:34px">Learn More</div>
</section>

<section class="services">
  <div class="section-tick" style="left:583px;top:1206px"></div>
  <h2 class="section-title" style="top:1244px;font-weight:400">Our Services</h2>

  <article class="service-card" style="left:142px">
    <svg class="icon" width="72" height="72" viewBox="0 0 72 72" fill="none" stroke="#5a2d91" stroke-width="2.2">
      <path d="M18 30L36 14l18 16 M22 27v17h28V27"/><rect x="31" y="32" width="10" height="12"/>
      <path d="M4 52h12l10 6h14c3 0 3 4 0 4H28 M16 64l14 4 30-12c3-1 2-5-1-4l-18 6"/>
    </svg>
    <h4>Estate Sales</h4>
    <p>Lorem Ipsum is simply dummy text of the printing and typesetting industry.</p>
    <div class="card-arrow"><svg width="20" height="12" viewBox="0 0 20 12"><path d="M0 6h18M13 1l5 5-5 5" stroke="#1b1b1b" stroke-width="2" fill="none"/></svg></div>
  </article>

  <article class="service-card" style="left:455px">
    <svg class="icon" width="72" height="72" viewBox="0 0 72 72" fill="none" stroke="#5a2d91" stroke-width="2.2">
      <rect x="10" y="34" width="10" height="30"/>
      <path d="M20 38l10-14V12c5 0 8 4 7 10l-2 10h16c4 0 5 5 2 7 3 2 2 6-1 7 2 2 1 6-2 7 1 3-1 6-4 6H26l-6-3"/>
      <path d="M52 6l2 6 6 2-6 2-2 6-2-6-6-2 6-2z M62 24l1 3 3 1-3 1-1 3-1-3-3-1 3-1z M14 14l1 3 3 1-3 1-1 3-1-3-3-1 3-1z"/>
    </svg>
    <h4>Cleanouts</h4>
    <p>Lorem Ipsum is simply dummy text of the printing and typesetting industry.</p>
    <div class="card-arrow"><svg width="20" height="12" viewBox="0 0 20 12"><path d="M0 6h18M13 1l5 5-5 5" stroke="#1b1b1b" stroke-width="2" fill="none"/></svg></div>
  </article>

  <article class="service-card" style="left:767px">
    <svg class="icon" width="72" height="72" viewBox="0 0 72 72" fill="none" stroke="#5a2d91" stroke-width="2.2">
      <rect x="12" y="8" width="48" height="60" rx="3"/><rect x="26" y="4" width="20" height="8" rx="2"/>
      <path d="M20 26l3 3 5-5 M20 40l3 3 5-5 M20 54l3 3 5-5 M34 27h18 M34 41h18 M34 55h18"/>
    </svg>
    <h4>Appraisals</h4>
    <p>Lorem Ipsum is simply dummy text of the printing and typesetting industry.</p>
    <div class="card-arrow"><svg width="20" height="12" viewBox="0 0 20 12"><path d="M0 6h18M13 1l5 5-5 5" stroke="#1b1b1b" stroke-width="2" fill="none"/></svg></div>
  </article>
</section>

<section class="testimonials">
  <div class="section-tick" style="left:583px;top:52px"></div>
  <h2 class="section-title" style="top:96px;font-weight:400">What Our Clients Say</h2>
</section>
<div class="avatar" style="left:496px;top:1834px;width:80px;height:80px;background:#b46b6e" role="img" aria-label="Client portrait"></div>
<div class="avatar" style="left:624px;top:1834px;width:80px;height:80px;background:#8a9a9c" role="img" aria-label="Client portrait"></div>
<div class="avatar" style="left:550px;top:1820px;width:100px;height:100px;background:#3f8a8a" role="img" aria-label="Client portrait"></div>
<svg class="abs" style="left:220px;top:1984px" width="28" height="14" viewBox="0 0 28 14"><path d="M28 7H2M8 1L2 7l6 6" stroke="#5a2d91" stroke-width="2" fill="none"/></svg>
<svg class="abs" style="left:952px;top:1984px" width="28" height="14" viewBox="0 0 28 14"><path d="M0 7h26M20 1l6 6-6 6" stroke="#5a2d91" stroke-width="2" fill="none"/></svg>
<p class="quote">It is a long established fact that a reader will be distracted by the readable content of a page when looking at its layout. The point of using Lorem Ipsum is that it has a more-or-less normal distribution of letters.</p>
<svg class="abs" style="left:552px;top:2051px" width="96" height="16" viewBox="0 0 96 16">
  <g fill="#fcd200"><path id="st" d="M8 0l2.4 5 5.4.6-4 3.7 1.1 5.4L8 12l-4.9 2.7 1.1-5.4-4-3.7 5.4-.6z"/>
  <use href="#st" x="20"/><use href="#st" x="40"/><use href="#st" x="60"/><use href="#st" x="80"/></g>
</svg>
<p class="abs" style="left:0;width:1200px;top:2078px;text-align:center;font-size:14px;font-weight:600">Daniel Whitfield</p>

<section class="upcoming">
  <div class="section-tick" style="left:583px;top:2234px"></div>
  <h2 class="section-title" style="top:2276px;font-weight:400">Upcoming Sales</h2>

  <article class="sale" style="left:141px">
    <div class="pic" role="img" aria-label="Modern two-storey house with lit garage at dusk" style="background:linear-gradient(180deg,#7d9fc4 0%,#4a5a78 45%,#c9b99b 70%,#b9b9b9 100%)"></div>
    <h5>Phoenix Reserve Estate Sale <svg width="16" height="14" viewBox="0 0 16 14"><path d="M8 14L1.5 7.5A4 4 0 018 2.2a4 4 0 016.5 5.3z" fill="#fcd200"/></svg></h5>
    <p class="loc"><svg width="10" height="14" viewBox="0 0 10 14"><path d="M5 14S0 8 0 5a5 5 0 0110 0c0 3-5 9-5 9z" fill="#5a2d91"/><circle cx="5" cy="5" r="2" fill="#fff"/></svg>Houston, Texas</p>
    <p class="date">February 8-11</p>
    <p class="more"><span>Learn More</span><svg width="18" height="10" viewBox="0 0 18 10"><path d="M0 5h16M12 1l4 4-4 4" stroke="#5a2d91" stroke-width="1.6" fill="none"/></svg></p>
  </article>

  <article class="sale" style="left:454px">
    <div class="pic" role="img" aria-label="Suburban brick homes under a clear blue sky" style="background:linear-gradient(180deg,#4f8fd1 0%,#a9c9e9 40%,#a58e79 62%,#5f7f3e 85%,#777 100%)"></div>
    <h5>Hacienda Estate Sale <svg width="16" height="14" viewBox="0 0 16 14"><path d="M8 14L1.5 7.5A4 4 0 018 2.2a4 4 0 016.5 5.3z" fill="#fcd200"/></svg></h5>
    <p class="loc"><svg width="10" height="14" viewBox="0 0 10 14"><path d="M5 14S0 8 0 5a5 5 0 0110 0c0 3-5 9-5 9z" fill="#5a2d91"/><circle cx="5" cy="5" r="2" fill="#fff"/></svg>Ft Worth, Texas</p>
    <p class="date">February 9-11</p>
    <p class="more"><span>Learn More</span><svg width="18" height="10" viewBox="0 0 18 10"><path d="M0 5h16M12 1l4 4-4 4" stroke="#5a2d91" stroke-width="1.6" fill="none"/></svg></p>
  </article>

  <article class="sale" style="left:767px">
    <div class="pic" role="img" aria-label="Contemporary villa with pool at evening" style="background:linear-gradient(180deg,#9bb3cf 0%,#d8d2c2 40%,#b8a78c 70%,#5d7fa8 100%)"></div>
    <h5>Sonoran Villa Estate Sale <svg width="16" height="14" viewBox="0 0 16 14"><path d="M8 14L1.5 7.5A4 4 0 018 2.2a4 4 0 016.5 5.3z" fill="#fcd200"/></svg></h5>
    <p class="loc"><svg width="10" height="14" viewBox="0 0 10 14"><path d="M5 14S0 8 0 5a5 5 0 0110 0c0 3-5 9-5 9z" fill="#5a2d91"/><circle cx="5" cy="5" r="2" fill="#fff"/></svg>San Antonio, Texas</p>
    <p class="date">February 9-11</p>
    <p class="more"><span>Learn More</span><svg width="18" height="10" viewBox="0 0 18 10"><path d="M0 5h16M12 1l4 4-4 4" stroke="#5a2d91" stroke-width="1.6" fill="none"/></svg></p>
  </article>
</section>

<footer>
  <svg class="abs" style="left:0;top:2795px" width="1200" height="446" viewBox="0 2795 1200 446">
    <polygon points="0,2906 600,2799 1200,2906 1200,2912 0,2912" fill="#fcd200"/>
    <polygon points="0,2912 600,2815 1200,2912 1200,3241 0,3241" fill="#1c1c1c"/>
  </svg>
  <div class="abs footer-mark"></div>
  <div class="abs footer-brand">Bright Haven<br><span style="font-size:20px;letter-spacing:3px">ESTATE SALES</span></div>

  <div class="footer-col" style="left:424px">
    <h6>Quick Links</h6>
    <a>Home</a><a>About Us</a><a>Services</a><a>Sales</a><a>FAQ’s</a><a>Resources</a>
  </div>
  <div class="footer-col" style="left:638px">
    <h6>Company</h6>
    <a>Terms &amp; Condition</a><a>Privacy Policy</a><a>Contact Us</a>
  </div>
  <div class="footer-col" style="left:848px;width:215px">
    <h6>Contact Info</h6>
    <div class="contact-row"><svg width="16" height="20" viewBox="0 0 16 20" style="flex:none"><path d="M8 16S2 10 2 6.5a6 6 0 0112 0C14 10 8 16 8 16z" fill="none" stroke="#fcd200" stroke-width="1.8"/><circle cx="8" cy="6.5" r="2.2" fill="#fcd200"/><path d="M2 19h12" stroke="#fcd200" stroke-width="1.8"/></svg><span>Address Line 1, Address Line 2, Address Line 3.</span></div>
    <div class="contact-row"><svg width="16" height="14" viewBox="0 0 16 14" style="flex:none;margin-top:3px"><rect width="16" height="12" rx="1.5" fill="#fcd200"/><path d="M1 1.5l7 5 7-5" stroke="#1c1c1c" stroke-width="1.4" fill="none"/></svg><span>info@brighthaven.example</span></div>
    <div class="contact-row"><svg width="16" height="16" viewBox="0 0 16 16" style="flex:none;margin-top:2px"><path d="M3 1l3 3-1.5 2.5c1 2 3 4 5 5L12 10l3 3-2 2C7 15 1 9 1 3z" fill="#fcd200"/></svg><span>615-555-0142</span></div>
  </div>

  <div class="abs footer-rule"></div>
  <p class="abs copyright">© 2024 Bright Haven Estate Sales. All Rights Reserved.</p>
  <span class="social" style="left:925px"></span>
  <span class="social" style="left:961px"></span>
  <span class="social" style="left:997px"></span>
  <span class="social" style="left:1033px"></span>
</footer>

</body>
</html>
```